4Star Hotel looking for web design

Hello everyone,
We are located in Cambodia, the hotel should open in 2-3 months. The name will be Velmora-Boutique Hotel. We are looking for a webdesign which is professional, elegant and SIMPLE.
All informations should be easy to find. We are quite open to proposition but we would like to the home page:
-a carousel with around 5-8 picture
-Little menu where we can book a room
By the way, we would like a page for our restaurant, gallery, contact page for description of the rooms. I add some old pictures.
I give an example of what we are expecting:
www.quenrostays.com/tovelspring
We hope that we are proposing a good job for you guys. Have fun and Thanks.
Oh and the winner ( or someone he had choose) of course have free night in our presidential suite
Target Market(s)
We are looking for european Market. Let s say people middle age who are willing to travel in difficult area
Industry/Entity Type
Hotel
Coding
Coded - Design and coding required
Number of Pages Required
5+ page
Requirements
Must have
- Simple, simple and Simple
- Carousel
- place for book a room
- during booking, a menu for select room , and after that another menu for propose like tour in town, taxi, flower, bottle of champagne for example
- during all the process, the customer should be able to know at what step it is and can stop and come back after
- Have to be perfect for smartphone
- Price with drawbar for they know how much they earn with our reduction
Nice to have
- during the process of information (name, adress, tel...), it would be great if they can fill it with a button facebook, google plus, lindkdin, instagram ....
- then a button share on facebook, twitter for know that they book in our hotel
- At the end of the booking, a flashcode with the recapitulatif that customer can scan.

```html
<!DOCTYPE html>
<html lang="en">
<head>
<meta charset="utf-8">
<title>Velmora-Boutique Hotel</title>
<link href="https://fonts.googleapis.com/css2?family=Open+Sans:ital,wght@0,400;0,600;0,700;1,400&family=Lora:ital@1&display=swap" rel="stylesheet">
<style>
:root{
  --orange:#ef7d22;
  --orange-dark:#d9651a;
  --brown:#3a1c12;
  --brown-mid:#6b2e1a;
  --brown-soft:#8a4a2c;
  --text:#4a4a4a;
  --muted:#8d8d8d;
  --line:#e2e2e2;
  --light:#f4f4f4;
  --white:#ffffff;
}
*{box-sizing:border-box;margin:0;padding:0}
html,body{width:1200px;height:2264px;overflow:hidden}
body{font-family:'Open Sans',Arial,sans-serif;color:var(--text);background:var(--white);position:relative;font-size:12px}
.container{width:960px;margin:0 auto;position:relative}
a{color:inherit;text-decoration:none}

/* top bar */
.top-bar{height:28px;background:var(--brown);color:#e9d8cf;font-size:11px}
.top-bar .container{display:flex;justify-content:flex-end;align-items:center;height:28px;gap:18px}
.top-social{display:flex;gap:5px}
.top-social span{width:16px;height:16px;background:var(--brown-soft);display:block}

/* nav */
.site-header{height:52px;background:var(--white);border-bottom:1px solid var(--line)}
.site-header .container{display:flex;justify-content:space-between;align-items:center;height:52px}
.brand{position:absolute;left:-10px;top:-28px;width:96px;height:80px;background:var(--brown);display:flex;flex-direction:column;align-items:center;justify-content:center;gap:5px;color:var(--white)}
.brand-dot{width:22px;height:22px;border-radius:50%;background:var(--orange)}
.brand-name{font-size:10px;font-weight:600;text-align:center;line-height:1.2}
.main-nav{margin-left:auto;display:flex;gap:22px;font-size:11px;font-weight:600;color:var(--brown);text-transform:uppercase;align-items:center}
.main-nav .active{color:var(--orange)}
.main-nav .cta{background:var(--orange);color:var(--white);padding:8px 12px}

/* hero */
.hero{height:392px;position:relative;background:linear-gradient(180deg,#9aa3a8 0%,#b8bfc2 35%,#7f8a78 52%,#4d6a3a 70%,#3a5a2c 100%)}
.hero-arrow{position:absolute;top:180px;width:22px;height:32px;background:rgba(0,0,0,.45);display:flex;align-items:center;justify-content:center}
.hero-arrow.prev{left:0}.hero-arrow.next{right:0}
.hero-caption{position:absolute;left:240px;top:160px;width:320px;background:rgba(176,74,28,.9);color:var(--white);padding:18px 20px}
.hero-caption h2{font-size:22px;font-weight:400;margin-bottom:8px}
.hero-caption p{font-size:11px;line-height:1.6;margin-bottom:14px;color:#fbe6d8}
.btn-outline{display:inline-block;border:1px solid var(--white);padding:6px 12px;font-size:10px;font-weight:600;text-transform:uppercase}

/* booking */
.booking{height:88px;background:var(--white)}
.booking-tabs{display:flex;font-size:10px;font-weight:700;text-transform:uppercase}
.booking-tabs span{padding:6px 14px;background:var(--orange);color:var(--white)}
.booking-tabs span+span{background:#f6d9c2;color:var(--brown-mid)}
.booking-form{background:#fbeee3;border-top:2px solid var(--orange);height:58px;display:flex;align-items:center;padding:0 14px;gap:12px}
.field{display:flex;flex-direction:column;gap:3px;font-size:9px;color:var(--brown-mid);font-weight:600}
.field .box{height:20px;background:var(--white);border:1px solid #ecd6c4}
.field.wide .box{width:170px}.field.small .box{width:90px}
.btn-search{margin-left:auto;margin-top:12px;background:var(--orange);color:var(--white);font-size:10px;font-weight:700;padding:6px 16px;text-transform:uppercase}

/* section heading */
.section-title{font-size:20px;color:var(--brown);font-weight:400;display:flex;align-items:center;gap:14px;margin-bottom:16px}
.section-title::after{content:"";flex:1;height:1px;background:var(--line)}
.view-all{position:absolute;right:0;top:4px;font-size:9px;border:1px solid var(--line);padding:3px 8px;background:var(--white);color:var(--muted);text-transform:uppercase}

/* offers */
.offers{padding-top:32px;height:232px}
.offer-grid{display:flex;gap:18px}
.offer-card{flex:1;height:136px;position:relative}
.offer-card:nth-child(1){background:linear-gradient(135deg,#7a3b22,#c1642f 60%,#3e2216)}
.offer-card:nth-child(2){background:linear-gradient(135deg,#c7a07a,#8d5a34 60%,#4b2a1a)}
.offer-card:nth-child(3){background:linear-gradient(135deg,#5a1d14,#b33a22 55%,#2e1410)}
.offer-label{position:absolute;left:0;bottom:0;background:rgba(30,14,8,.78);color:var(--white);padding:6px 10px;font-size:10px;font-weight:700;text-transform:uppercase;line-height:1.4}
.offer-label del{color:#d6b9a6;font-weight:400;margin-right:4px}
.offer-label b{color:var(--orange)}

/* facilities */
.facilities{height:220px}
.facility-grid{display:flex;gap:24px;text-align:center}
.facility{flex:1}
.facility svg{display:block;margin:0 auto 8px}
.facility h3{font-size:13px;font-weight:600;color:var(--brown);margin-bottom:6px}
.facility p{font-size:10px;line-height:1.6;color:var(--muted);margin-bottom:8px}
.read-more{font-size:10px;color:var(--orange);font-weight:600}

/* gallery */
.gallery-head{height:52px}
.gallery-strip{display:flex;height:260px}
.gallery-strip div{flex:1}
.gallery-strip div:nth-child(1){background:linear-gradient(160deg,#8c4a24,#c07a42 50%,#5e2c16)}
.gallery-strip div:nth-child(2){background:linear-gradient(180deg,#c9d2d8,#a07a5a 45%,#6d4a30)}
.gallery-strip div:nth-child(3){background:linear-gradient(160deg,#d8a066,#b56a32 55%,#7a3e1e)}
.gallery-strip div:nth-child(4){background:linear-gradient(160deg,#c2752d,#9c4f1e 60%,#5a2a12)}
.gallery-strip div:nth-child(5){background:linear-gradient(160deg,#e8dfd2,#c9b8a2 50%,#8a7a68)}
.gallery-captions{display:flex;height:48px;padding-top:10px}
.gallery-captions span{flex:1;padding-left:16px;font-size:10px;color:var(--orange);line-height:1.4}
.gallery-captions small{display:block;color:var(--muted);font-size:9px}

/* blog */
.blog{background:var(--light);height:386px;padding-top:28px;margin-top:12px}
.blog-grid{display:flex;gap:24px}
.post{flex:1}
.post-image{height:132px;margin-bottom:10px}
.post:nth-child(1) .post-image{background:linear-gradient(160deg,#5a2a1a,#a9643a 55%,#e1c7a3)}
.post:nth-child(2) .post-image{background:linear-gradient(180deg,#8fb6d8,#b7c6b0 45%,#7d6a3e 75%,#4d6a32)}
.post:nth-child(3) .post-image{background:linear-gradient(180deg,#6aa1d4,#9ec2e0 40%,#d2a24a 65%,#7b5a2a)}
.post h3{font-size:13px;font-weight:600;color:var(--brown);margin-bottom:3px}
.post time{font-size:9px;color:var(--muted);display:block;margin-bottom:6px}
.post p{font-size:10px;line-height:1.6;color:var(--muted);margin-bottom:6px}

/* testimonial */
.testimonial{height:240px;background:linear-gradient(90deg,#ee7a22,#f39a4c 50%,#ec7420);color:var(--white);text-align:center;padding-top:42px;margin-top:18px}
.quote-mark{width:34px;height:34px;border-radius:50%;background:var(--white);color:var(--orange);margin:0 auto 16px;font-family:'Lora',serif;font-size:26px;line-height:40px}
.testimonial blockquote{font-family:'Lora',serif;font-style:italic;font-size:14px;line-height:1.7;width:560px;margin:0 auto 14px}
.testimonial cite{font-style:normal;font-size:12px;font-weight:600;display:block;margin-bottom:6px}
.stars{letter-spacing:3px;font-size:13px}

/* footer */
.site-footer{height:202px;background:var(--brown);color:#cdb3a5;padding-top:26px}
.footer-grid{display:flex;gap:28px}
.footer-col{flex:1;font-size:10px;line-height:1.7}
.footer-col h4{color:var(--white);font-size:11px;font-weight:700;text-transform:uppercase;margin-bottom:10px}
.social-row{display:flex;gap:6px;margin-bottom:16px}
.social-row span{width:24px;height:24px;border-radius:50%;background:var(--orange);display:block}
.footer-col ul{list-style:none}
.footer-col li{padding-left:10px;position:relative}
.footer-col li::before{content:"›";position:absolute;left:0;color:var(--orange)}
.tweet{margin-bottom:8px}
.tweet b{color:var(--orange);font-weight:400}
.footer-bottom{height:34px;background:#2a130c;color:#9c8074;font-size:9px}
.footer-bottom .container{display:flex;justify-content:flex-start;align-items:center;height:34px}
</style>
</head>
<body>

<div class="top-bar">
  <div class="container">
    <span>+855 12 480 316</span>
    <span>stay@velmorahotel.example</span>
    <div class="top-social"><span></span><span></span><span></span><span></span></div>
  </div>
</div>

<header class="site-header">
  <div class="container">
    <a class="brand" href="#"><span class="brand-dot"></span><span class="brand-name">Velmora-Boutique<br>Hotel</span></a>
    <nav class="main-nav">
      <a class="active" href="#">Home</a>
      <a href="#">Accommodation</a>
      <a href="#">Restaurant &amp; Bar</a>
      <a href="#">Meetings &amp; Events</a>
      <a href="#">Blog</a>
      <a class="cta" href="#">Contact Us</a>
    </nav>
  </div>
</header>

<section class="hero" role="img" aria-label="Carousel photo of a wide lake surrounded by green forest under a grey sky">
  <span class="hero-arrow prev"><svg width="8" height="12" viewBox="0 0 8 12"><path d="M7 1 2 6l5 5" fill="none" stroke="#fff" stroke-width="2"/></svg></span>
  <span class="hero-arrow next"><svg width="8" height="12" viewBox="0 0 8 12"><path d="M1 1l5 5-5 5" fill="none" stroke="#fff" stroke-width="2"/></svg></span>
  <div class="hero-caption">
    <h2>Kingdom of Cambodia</h2>
    <p>Discover calm lakes, red earth roads and old forest trails. Rest well in our quiet rooms after a long day of travel.</p>
    <a class="btn-outline" href="#">View More Details</a>
  </div>
</section>

<section class="booking">
  <div class="container">
    <div class="booking-tabs"><span>Search Rooms</span><span>Accommodation</span></div>
    <form class="booking-form">
      <label class="field wide">Arrival<span class="box"></span></label>
      <label class="field wide">Departure<span class="box"></span></label>
      <label class="field small">Rooms<span class="box"></span></label>
      <label class="field small">Adults<span class="box"></span></label>
      <label class="field small">Children<span class="box"></span></label>
      <span class="btn-search">Search Now</span>
    </form>
  </div>
</section>

<section class="offers">
  <div class="container">
    <h2 class="section-title">Special Offers</h2>
    <div class="offer-grid">
      <article class="offer-card" role="img" aria-label="Photo of a warmly lit hotel dining room"><div class="offer-label">Special Offer Title<br><del>$120</del><b>$89</b></div></article>
      <article class="offer-card" role="img" aria-label="Photo of a hotel bedroom with wooden furniture"><div class="offer-label">Bed &amp; Breakfast<br><del>$95</del><b>$72</b></div></article>
      <article class="offer-card" role="img" aria-label="Photo of a red restaurant interior"><div class="offer-label">Restaurant Offer<br><del>$40</del><b>$29</b></div></article>
    </div>
  </div>
</section>

<section class="facilities">
  <div class="container">
    <h2 class="section-title">Our Facilities</h2>
    <div class="facility-grid">
      <div class="facility">
        <svg width="30" height="30" viewBox="0 0 30 30"><path d="M15 3a8 8 0 0 0-8 8c0 6 8 16 8 16s8-10 8-16a8 8 0 0 0-8-8z" fill="none" stroke="#ef7d22" stroke-width="2"/><circle cx="15" cy="11" r="3" fill="#ef7d22"/></svg>
        <h3>Book Your Trip</h3>
        <p>Plan your stay with us and add local tours, taxi rides and small gifts in one easy step.</p>
        <a class="read-more" href="#">Read More »</a>
      </div>
      <div class="facility">
        <svg width="30" height="30" viewBox="0 0 30 30"><rect x="6" y="5" width="18" height="21" fill="none" stroke="#ef7d22" stroke-width="2"/><path d="M10 10h3M17 10h3M10 15h3M17 15h3M13 26v-5h4v5" stroke="#ef7d22" stroke-width="2" fill="none"/></svg>
        <h3>Velmora Boutique Hotel</h3>
        <p>Elegant rooms, a calm garden and a warm team ready to help you at any hour of the day.</p>
        <a class="read-more" href="#">Read More »</a>
      </div>
      <div class="facility">
        <svg width="30" height="30" viewBox="0 0 30 30"><rect x="4" y="8" width="22" height="15" fill="none" stroke="#ef7d22" stroke-width="2"/><path d="M4 8l11 9 11-9" fill="none" stroke="#ef7d22" stroke-width="2"/></svg>
        <h3>Discover Cambodia</h3>
        <p>Ancient temples, lively markets and wide rivers wait for you just a short drive away.</p>
        <a class="read-more" href="#">Read More »</a>
      </div>
      <div class="facility">
        <svg width="30" height="30" viewBox="0 0 30 30"><path d="M4 6h16v10H10l-4 4v-4H4z" fill="none" stroke="#ef7d22" stroke-width="2"/><path d="M22 11h4v10h-2v4l-4-4h-8v-3" fill="none" stroke="#ef7d22" stroke-width="2"/></svg>
        <h3>24/7 Support</h3>
        <p>Call or write to us whenever you need help before, during or after your stay here.</p>
        <a class="read-more" href="#">Read More »</a>
      </div>
    </div>
  </div>
</section>

<section class="gallery">
  <div class="container gallery-head">
    <h2 class="section-title">Gallery</h2>
    <a class="view-all" href="#" style="top:30px">View Gallery</a>
  </div>
  <div class="gallery-strip">
    <div role="img" aria-label="Photo of a wooden staircase with carved railing"></div>
    <div role="img" aria-label="Photo of the hotel building front with balconies"></div>
    <div role="img" aria-label="Photo of a warm wooden hallway"></div>
    <div role="img" aria-label="Photo of a lobby corridor in orange light"></div>
    <div role="img" aria-label="Photo of a stone statue in a pale hall"></div>
  </div>
  <div class="gallery-captions">
    <span>Gallery Photo<small>Grand stairway</small></span>
    <span>Gallery Photo<small>Hotel front</small></span>
    <span>Gallery Photo<small>Upper hallway</small></span>
    <span>Gallery Photo<small>Lobby corridor</small></span>
    <span>Gallery Photo<small>Main hall</small></span>
  </div>
</section>

<section class="blog">
  <div class="container">
    <h2 class="section-title">From the Blog</h2>
    <a class="view-all" href="#">View All</a>
    <div class="blog-grid">
      <article class="post">
        <div class="post-image" role="img" aria-label="Photo of a set restaurant table"></div>
        <h3>Top 10 Hotels in Cambodia</h3>
        <time>January 12, 2015</time>
        <p>A short guide to calm places to stay while you travel across the north east of the country.</p>
        <a class="read-more" href="#">Read More »</a>
      </article>
      <article class="post">
        <div class="post-image" role="img" aria-label="Photo of an ancient temple behind a pond"></div>
        <h3>Top 10 Places to Visit</h3>
        <time>January 08, 2015</time>
        <p>From old temples to quiet waterfalls, here are the sights our guests love the most each year.</p>
        <a class="read-more" href="#">Read More »</a>
      </article>
      <article class="post">
        <div class="post-image" role="img" aria-label="Photo of a golden palace roof under blue sky"></div>
        <h3>Top 10 Palaces in Cambodia</h3>
        <time>January 03, 2015</time>
        <p>Golden roofs, bright gardens and rich history to explore on a slow day trip from the city.</p>
        <a class="read-more" href="#">Read More »</a>
      </article>
    </div>
  </div>
</section>

<section class="testimonial" role="img" aria-label="Soft orange backdrop photo of happy guests">
  <div class="quote-mark">“</div>
  <blockquote>A lovely stay with a kind team, clean rooms and great food. We will surely come back on our next trip to Cambodia.</blockquote>
  <cite>Member | Travel Guest</cite>
  <div class="stars">★★★★★</div>
</section>

<footer class="site-footer">
  <div class="container footer-grid">
    <div class="footer-col">
      <h4>Find Us Online</h4>
      <div class="social-row"><span></span><span></span><span></span><span></span></div>
      <h4>Location</h4>
      <p>No. 14 Lumora Street, Banlung<br>Ratanak Province, Cambodia<br>+855 12 480 316</p>
    </div>
    <div class="footer-col">
      <h4>Location</h4>
      <p>No. 22 Sokhen Avenue<br>Phnom Penh, Cambodia<br>+855 23 715 204<br>stay@velmorahotel.example</p>
    </div>
    <div class="footer-col" style="flex:1.3">
      <h4>Tweets</h4>
      <p class="tweet">New garden suites open this season, book early. <b>2 hours ago</b></p>
      <p class="tweet">Join our sunset boat trip on the lake this week. <b>1 day ago</b></p>
      <p class="tweet">Fresh local dishes now on our dinner menu. <b>3 days ago</b></p>
    </div>
    <div class="footer-col">
      <h4>Accommodation</h4>
      <ul>
        <li>Deluxe Room</li>
        <li>Superior Room</li>
        <li>Family Room</li>
        <li>Junior Suite</li>
        <li>Presidential Suite</li>
      </ul>
    </div>
  </div>
</footer>
<div class="footer-bottom">
  <div class="container">
    <span>© 2015 Velmora-Boutique Hotel. All rights reserved.</span>
  </div>
</div>

</body>
</html>
```